Business card for a plastic surgeon

i need a business card for a plastic surgeon. I have two adresses. The card should communicate safety, simmetry, beauty and with soft colors.
What i want in the card:
- my logo: Letters "R"and "B" (picture uploaded)
- my name: Renato Bastiani
- my registration: CRM 507 219
- my adresses and phone numbers (2):
- Av Dr Teixeira Lopes, 2710, sala 305 - Vila Olímpia | São Paulo/ SP - Phone: 11 4172-5036
- Al. Itapeva, 47, 3 andar - Alphaville | Barueri/ SP - Phone: 11 6350-2481

- my social network: site, facebook and instagram

Target Market(s)

people (95% girls and women) that want cosmetic procedures and plastic surgery

Industry/Entity Type

Business

Contact Information for Business Card

The card should communicate safety, simmetry, beauty and with soft colors.
Beige, brown, gray, rosy are some options. Color is free

Font styles to use
Serif

Requirements
Must have
• - my logo: Letters "R"and "B" (picture uploaded)
• - my name: Renato Bastiani
• - my registration: CRM 507 219
• - my adresses and phone numbers (2):
• - Av Dr Teixeira Lopes, 2710, sala 305 - Vila Olímpia | São Paulo/ SP - Phone: 11 4172-5036
• - Al. Itapeva, 47, 3 andar - Alphaville | Barueri/ SP - Phone: 11 6350-2481
• - my social network: site, facebook and instagram
Should not have
• other images (only my logo)

```html
<!DOCTYPE html>
<html lang="pt-BR">
<head>
<meta charset="utf-8">
<title>Dr. Renato Bastiani – Cartão de visita</title>
<link rel="stylesheet" href="https://fonts.googleapis.com/css2?family=Marcellus&family=PT+Serif&display=swap">
<style>
  :root {
    --stage: #b1aeae;
    --brown-deep: #2c190c;
    --brown-mid: #3a2414;
    --glow: #a8927a;
    --ivory: #ece6dd;
    --taupe: #a89378;
    --ink: #2b1a0e;
    --paper: #ffffff;
    --faint: #ebe6e0;
  }
  * { margin: 0; padding: 0; box-sizing: border-box; }
  html, body { width: 924px; height: 1200px; overflow: hidden; }
  body { background: var(--stage); position: relative; font-family: "PT Serif", Georgia, serif; }

  .card { position: absolute; left: 100px; width: 728px; overflow: hidden; box-shadow: 0 30px 40px -20px rgba(40,30,30,.45); }

  .card-front {
    top: 70px; height: 460px;
    background: radial-gradient(circle at 51% 46%, var(--glow) 0%, #6b523c 14%, var(--brown-mid) 32%, var(--brown-deep) 60%);
  }
  .front-mark { position: absolute; left: 335px; top: 205px; width: 70px; height: 70px; border: 2px solid var(--ivory); border-radius: 50%; }
  .brand-name {
    position: absolute; left: 0; width: 100%; text-align: center;
    font-family: "Marcellus", serif; text-transform: uppercase; color: var(--ivory);
  }
  .card-front .brand-name { top: 283px; font-size: 31px; letter-spacing: .5px; }
  .brand-title {
    position: absolute; left: 0; width: 100%; text-align: center;
    font-family: "Marcellus", serif; text-transform: uppercase; color: var(--ivory);
  }
  .card-front .brand-title { top: 322px; font-size: 16px; letter-spacing: 3.5px; }

  .card-back { top: 641px; height: 459px; background: var(--paper); }
  .side-tab { position: absolute; left: 0; top: 192px; width: 26px; height: 232px; background: var(--brown-deep); border-radius: 0 6px 6px 0; }
  .person-name { position: absolute; left: 50px; top: 66px; font-size: 30px; color: var(--ink); }
  .registration { position: absolute; left: 52px; top: 123px; font-size: 22px; color: var(--taupe); }

  .location { position: absolute; left: 56px; font-size: 20px; line-height: 30px; color: var(--ink); }
  .location.first { top: 206px; }
  .location.second { top: 311px; }
  .location li { list-style: none; position: relative; padding-left: 22px; }
  .location svg { position: absolute; left: 0; }

  .social { position: absolute; left: 470px; top: 40px; font-size: 17px; color: var(--ink); }
  .social li { list-style: none; position: relative; padding-left: 30px; height: 34px; line-height: 28px; }
  .social li::before { content: ""; position: absolute; left: 1px; top: 5px; width: 19px; height: 19px; border-radius: 50%; background: var(--taupe); }

  .back-mark { position: absolute; left: 573px; top: 182px; width: 44px; height: 44px; border: 2px solid var(--ink); border-radius: 50%; }
  .card-back .brand-name { left: 470px; width: 246px; top: 302px; font-size: 21px; color: var(--ink); }
  .card-back .brand-title { left: 470px; width: 246px; top: 328px; font-size: 11px; letter-spacing: 2.6px; color: var(--ink); }
</style>
</head>
<body>
  <section class="card card-front" aria-label="Frente do cartão">
    <div class="front-mark" aria-hidden="true"></div>
    <p class="brand-name">Dr. Renato Bastiani</p>
    <p class="brand-title">Cirurgião Plástico</p>
  </section>

  <section class="card card-back" aria-label="Verso do cartão">
    <div class="side-tab"></div>
    <h1 class="person-name">Renato Bastiani</h1>
    <p class="registration">CRM 507 219</p>

    <ul class="location first">
      <li>
        <svg width="16" height="26" viewBox="0 0 16 26" style="top:6px"><path d="M8 1a6 6 0 0 0-6 6c0 4.5 6 11 6 11s6-6.5 6-11a6 6 0 0 0-6-6z" fill="var(--taupe)"/><circle cx="8" cy="7" r="2.3" fill="#fff"/><rect x="1" y="23" width="14" height="2" fill="var(--taupe)"/></svg>
        Av Dr Teixeira Lopes, 2710, sala<br>305 - Vila Olímpia | São Paulo/ SP
      </li>
      <li>
        <svg width="14" height="20" viewBox="0 0 14 20" style="top:6px"><path d="M9 1C5 3 2 8 4 15c1 3 4 4 5 2l-1-3c-1 1-2 0-2-1-1-4 0-7 2-9l1 1 2-3z" fill="var(--taupe)"/></svg>
        11 4172-5036
      </li>
    </ul>

    <ul class="location second">
      <li>
        <svg width="16" height="26" viewBox="0 0 16 26" style="top:6px"><path d="M8 1a6 6 0 0 0-6 6c0 4.5 6 11 6 11s6-6.5 6-11a6 6 0 0 0-6-6z" fill="var(--ink)"/><circle cx="8" cy="7" r="2.3" fill="#fff"/><rect x="1" y="23" width="14" height="2" fill="var(--taupe)"/></svg>
        Al. Itapeva, 47, 3 andar Al-<br>phaville | Barueri/ SP
      </li>
      <li>
        <svg width="14" height="20" viewBox="0 0 14 20" style="top:6px"><path d="M9 1C5 3 2 8 4 15c1 3 4 4 5 2l-1-3c-1 1-2 0-2-1-1-4 0-7 2-9l1 1 2-3z" fill="var(--ink)"/></svg>
        11 6350-2481
      </li>
    </ul>

    <ul class="social">
      <li>www.renatobastiani.com</li>
      <li>info@bastianiclinica.com</li>
      <li>@drrenatobastiani</li>
    </ul>

    <div class="back-mark" aria-hidden="true"></div>
    <p class="brand-name">Dr. Renato Bastiani</p>
    <p class="brand-title">Cirurgião Plástico</p>
  </section>
</body>
</html>
```